Full Page Appliance Ad

Create a full page ad (7.5" W x 10" H) representing that we are a full service appliance company, where we have a showroom located at 14 N. Birch Lane Harlow Springs, PA 17999. Our website is www.qrtolvek.com , and our phone number is 555-555-0148. We don't only sell appliances, we deliver, install, and service. We also offer an additional year warranty* (see store for details). In addition to appliances, we also have an Electrical Department that specializes in residential applications.
May be best if split the full page ad into two spots. One spot to reference appliances, and the other to represent electrical.
I want it to look clean, and not too busy
Target Market(s)
30-70 years old
Look and feel

```html
<!DOCTYPE html>
<html lang="en">
<head>
<meta charset="utf-8">
<title>Qrtolvek – Full Page Appliance Ad</title>
<link href="https://fonts.googleapis.com/css2?family=Anton&family=Allura&display=swap" rel="stylesheet">
<style>
  :root{
    --navy:#15163a;
    --orange:#f3a21d;
    --charcoal:#3b3b3d;
    --white:#ffffff;
    --backdrop:#eef0f2;
    --photo-mid:#b9bbbe;
    --photo-dark:#6f7175;
    --icon-grey:#8a8ca6;
  }
  *{margin:0;padding:0;box-sizing:border-box}
  html,body{width:1200px;height:1077px;overflow:hidden;background:var(--backdrop)}
  .ad{
    position:absolute;left:211px;top:20px;width:778px;height:1037px;
    background:var(--white);overflow:hidden;
    font-family:'Anton',sans-serif;color:var(--navy);
    box-shadow:0 4px 18px rgba(0,0,0,.12);
  }
  .brand-tab{
    position:absolute;left:60px;top:0;width:420px;height:100px;
    background:var(--navy);border-radius:0 0 60px 60px;
    display:flex;align-items:center;justify-content:center;gap:14px;
  }
  .brand-dot{width:34px;height:34px;border-radius:50%;background:var(--white)}
  .brand-name{color:var(--white);font-size:34px;letter-spacing:2px;text-transform:uppercase}
  .headline{
    position:absolute;left:48px;top:122px;font-size:46px;line-height:1.02;
    text-transform:uppercase;letter-spacing:.5px;
  }
  .headline .accent{color:var(--orange)}
  .appliance-photo{
    position:absolute;left:130px;top:250px;width:648px;height:450px;
    background:radial-gradient(ellipse at 55% 45%, var(--photo-dark) 0%, var(--photo-mid) 40%, rgba(255,255,255,0) 72%);
  }
  .services{position:absolute;top:700px;left:0;width:778px;height:70px}
  .service{position:absolute;display:flex;align-items:flex-end;gap:6px}
  .service svg{width:34px;height:30px;margin-bottom:18px}
  .service .we{font-family:'Allura',cursive;font-size:40px;line-height:1}
  .service .verb{font-size:32px;line-height:1.1;text-transform:uppercase}
  .service.deliver{left:150px}
  .service.install{left:360px}
  .service.service-item{left:570px}
  .electrical{
    position:absolute;left:300px;top:790px;width:478px;height:84px;
    background:var(--charcoal);clip-path:polygon(22px 0,100% 0,100% 100%,0 100%);
    color:var(--white);font-size:19px;line-height:1.2;text-transform:uppercase;
    padding:14px 30px 0 54px;
  }
  .electrical .flag{color:var(--orange)}
  .contact-band{
    position:absolute;left:0;top:874px;width:778px;height:163px;background:var(--navy);
    color:var(--white);
  }
  .contact{position:absolute;display:flex;align-items:center;gap:10px;text-transform:uppercase;white-space:nowrap}
  .contact svg{width:22px;height:26px;fill:none;stroke:var(--icon-grey);stroke-width:2}
  .contact.phone{left:310px;top:28px;font-size:32px}
  .contact.web{left:520px;top:32px;font-size:28px;color:var(--orange)}
  .contact.address{left:310px;top:88px;font-size:24px}
  .warranty-badge{
    position:absolute;left:30px;top:760px;width:250px;height:250px;border-radius:50%;
    background:var(--orange);display:flex;align-items:center;justify-content:center;
  }
  .warranty-ring{
    width:206px;height:206px;border-radius:50%;border:5px solid var(--white);
    display:flex;flex-direction:column;align-items:center;justify-content:center;
    color:var(--navy);text-transform:uppercase;text-align:center;
  }
  .warranty-ring .small{font-size:17px;letter-spacing:1px}
  .warranty-ring .big{font-size:56px;line-height:1}
  .warranty-ring .mid{font-size:30px;line-height:1.05}
  .warranty-ring .fine{font-size:10px;letter-spacing:1px}
</style>
</head>
<body>
<main class="ad">
  <header class="brand-tab">
    <span class="brand-dot"></span>
    <span class="brand-name">Qrtolvek</span>
  </header>

  <h1 class="headline">Experience hassle-free living<br>with our <span class="accent">full-service</span><br><span class="accent">appliances</span></h1>

  <div class="appliance-photo" role="img" aria-label="Stainless steel appliances grouped together: microwave, range, dishwasher, refrigerator, vacuum, iron and front-load washer"></div>

  <section class="services">
    <div class="service deliver">
      <svg viewBox="0 0 34 30" fill="none" stroke="#15163a" stroke-width="2.2"><path d="M8 6h16v14H8zM24 11h5l4 5v4h-9"/><circle cx="12" cy="23" r="3"/><circle cx="27" cy="23" r="3"/><path d="M1 10h5M3 14h4"/></svg>
      <span class="we">We</span><span class="verb">Deliver</span>
    </div>
    <div class="service install">
      <svg viewBox="0 0 34 30" fill="#15163a"><path d="M4 6l8 8-3 3-8-8a5 5 0 0 1 3-3zM30 6l-8 8 3 3 8-8a5 5 0 0 0-3-3z"/><rect x="11" y="16" width="12" height="12" rx="3"/></svg>
      <span class="we">We</span><span class="verb">Install</span>
    </div>
    <div class="service service-item">
      <svg viewBox="0 0 34 30" fill="none" stroke="#15163a" stroke-width="2.2"><circle cx="17" cy="9" r="6"/><path d="M6 29c0-7 5-11 11-11s11 4 11 11"/></svg>
      <span class="we">We</span><span class="verb">Service</span>
    </div>
  </section>

  <p class="electrical"><span class="flag">Available!</span> Electrical department that<br>specializes in residential applications</p>

  <footer class="contact-band">
    <div class="contact phone">
      <svg viewBox="0 0 22 26"><rect x="3" y="1" width="16" height="24" rx="3"/><path d="M9 21h4"/></svg>
      <span>555-555-0148</span>
    </div>
    <div class="contact web">
      <svg viewBox="0 0 26 26"><circle cx="13" cy="13" r="11"/><path d="M2 13h22M13 2c-6 7-6 15 0 22M13 2c6 7 6 15 0 22"/></svg>
      <span>www.qrtolvek.com</span>
    </div>
    <div class="contact address">
      <svg viewBox="0 0 22 26"><path d="M11 25s-8-9-8-15a8 8 0 0 1 16 0c0 6-8 15-8 15z"/><circle cx="11" cy="10" r="3"/></svg>
      <span>14 N. Birch Lane Harlow Springs, PA 17999</span>
    </div>
  </footer>

  <div class="warranty-badge">
    <div class="warranty-ring">
      <span class="small">Additional</span>
      <span class="big">1 Year</span>
      <span class="mid">Warranty*</span>
      <span class="fine">See store for details</span>
    </div>
  </div>
</main>
</body>
</html>
```